Construction Company

Design a clutter free business card, it can be double-sided utilizing the logo for BDN Ltd simple with all relevant contact information.

Please also a letterhead design to function for the purposes of invoicing, all mail requirements, with header to be distinctive while the footer ties page together and incorporates all necessary information.

For now, please use generic / dummy text and when a winner is selected, I will disclose the contact information.

Hi Designers! Please read the updated brief which includes the design of a business card and letterhead. Thank you!

```html
<!DOCTYPE html>
<html lang="en">
<head>
<meta charset="UTF-8">
<title>BDN Ltd — Business Card</title>
<link href="https://fonts.googleapis.com/css2?family=Open+Sans:wght@400;600;700&display=swap" rel="stylesheet">
<style>
  :root {
    --canvas: #1c1c1f;
    --card-blue: #263b8c;
    --card-blue-light: #2f4aa6;
    --gold: #c39a36;
    --white: #ffffff;
  }
  * { box-sizing: border-box; margin: 0; padding: 0; }
  html, body {
    width: 1200px; height: 900px; overflow: hidden;
    background: var(--canvas);
    font-family: "Open Sans", Arial, sans-serif;
  }
  .canvas {
    width: 1200px; height: 900px;
    display: flex; flex-direction: column;
    align-items: center; justify-content: center; gap: 60px;
  }
  .card {
    width: 560px; height: 320px;
    background: var(--card-blue);
    position: relative;
    box-shadow: 0 12px 30px rgba(0,0,0,.45);
  }
  /* front */
  .card-front .brand {
    position: absolute; left: 48px; top: 118px;
    display: flex; align-items: center; gap: 12px;
  }
  .brand-dot {
    width: 16px; height: 16px; border-radius: 50%;
    background: var(--gold);
  }
  .brand-name {
    font-weight: 700; font-size: 44px; color: var(--white);
    letter-spacing: 1px; line-height: 1;
  }
  .divider {
    position: absolute; left: 292px; top: 60px;
    width: 1.5px; height: 200px; background: var(--gold);
  }
  .contact {
    position: absolute; left: 312px; top: 72px;
    color: var(--white); font-size: 13px; line-height: 1.45;
  }
  .contact .person-name {
    color: var(--gold); font-weight: 700; font-size: 17px;
    letter-spacing: .5px; text-transform: uppercase;
  }
  .contact .person-title { font-size: 14px; margin-bottom: 6px; }
  .contact .address { margin-bottom: 6px; }
  .contact-line { display: flex; align-items: center; gap: 8px; }
  .contact-line svg { width: 11px; height: 11px; flex: none; }
  /* back */
  .card-back .brand-faint {
    position: absolute; inset: 0;
    display: flex; align-items: center; justify-content: center;
    font-weight: 700; font-size: 92px; letter-spacing: 4px;
    color: var(--card-blue-light);
  }
</style>
</head>
<body>
<main class="canvas">
  <section class="card card-front" aria-label="Business card front">
    <div class="brand">
      <span class="brand-dot"></span>
      <span class="brand-name">BDN Ltd</span>
    </div>
    <div class="divider"></div>
    <div class="contact">
      <p class="person-name">Daniel Harlow</p>
      <p class="person-title">President</p>
      <p class="address">1820 Harbor View Road<br>Seacliff CA 90210</p>
      <p class="contact-line">
        <svg viewBox="0 0 12 12" aria-hidden="true"><path fill="#c39a36" d="M2.5 0.5l2 2.2-1 1.3c.6 1.5 1.9 2.8 3.4 3.4l1.3-1 2.3 2-1.3 2.1C5 10.3 1.7 7 .4 1.8z"/></svg>
        555-014-2287
      </p>
      <p class="contact-line">
        <svg viewBox="0 0 12 12" aria-hidden="true"><rect x="0.5" y="2" width="11" height="8" fill="#c39a36"/><path d="M0.5 2l5.5 4.5L11.5 2" fill="none" stroke="#263b8c" stroke-width="1"/></svg>
        dharlow@bdnltd.com
      </p>
      <p class="contact-line">
        <svg viewBox="0 0 12 12" aria-hidden="true"><circle cx="6" cy="6" r="5.3" fill="none" stroke="#c39a36" stroke-width="1.2"/><ellipse cx="6" cy="6" rx="2.2" ry="5.3" fill="none" stroke="#c39a36" stroke-width="1"/><line x1="0.7" y1="6" x2="11.3" y2="6" stroke="#c39a36" stroke-width="1"/></svg>
        www.bdnltd.com
      </p>
    </div>
  </section>

  <section class="card card-back" aria-label="Business card back">
    <div class="brand-faint">BDN Ltd</div>
  </section>
</main>
</body>
</html>
```